Construction Company Website Design

I need a Website Design for a Construction Company. I have attached logo and business card design files (a.i) to match styles and text for the website. I will need design for 3 pages:
1. A Home page
2. A secondary page (will be different information pages)
3. A contact page with submision form
Website to look professional and match the 'theme' across all pages, using main colours / reverse colours as per design files. Must be clear it is a construction related website without being over the top. Happy for the construction related details (whether that be images/outlines/backgrounds etc to be fairly subtle and not overbearing on the contect of the pages. It will be the content that will be most important, not the images within.

Content has not yet been fully completed but attached is a site map. Each page will need a space for the insertion of the relevant heading and associated content for that particular page. Example can be used as per attached map. If it is preferable to have content completed for this to be a more succesful project please advise and I will complete and submit.

Target Market(s)

Clients for potential construction projects. These could be a range of people. All would be very professional, well educated and put a substantial expection on the quality of website provided.

Industry/Entity Type

Construction

Number of Pages Required

3 page

Font styles to use
Serif
Sans Serif
Other font styles liked:
• fonts preferable as per design files provided unless designer beleives a different font would suit better

Requirements
Must have
• Colour scheme to match logo and business card files provided. Fonts that match as per provided files. Pages must be consistent with the theme carrying across all pages. All pages must have contact details at the bottom of the page.
• Contents of page 1 - 'Home page': multiple tab options / logo link
• Contents of page 2 - 'Secondary page': Top and side navigation / area for information and/or images.
• Contents of page - 'Contact us page': Top and side navigation / Submission form / area for logos such as linkdin, facebook etc.
Nice to have
• Would be good to have a or some generic construction related images - outlines / shadows / effects etc. These might be background images or outlines related to the relevant industry and are consistent across the pages. Could be outlines of buildings, images of men with hardhats etc etc. Good to see colour scheme as per design files used
Should not have
• No pictures of houses. Generally no photos. If any imagery of people must not show faces/details.

```html
<!DOCTYPE html>
<html lang="en">
<head>
<meta charset="utf-8">
<title>Kestrel Constructions</title>
<link rel="stylesheet" href="https://fonts.googleapis.com/css2?family=Rajdhani:wght@500;600&display=swap">
<style>
  :root {
    --frame: #e6e6e6;
    --night: #121315;
    --slate: #2b3138;
    --steel: #4a5a63;
    --teal: #3f6e66;
    --accent: #1a96d4;
    --nav-text: #c9ccd0;
    --logo-text: #8c9197;
    --heading: #e4e7ea;
    --lead: #b4bac0;
    --footer-bg: #ffffff;
    --footer-text: #7a7a7a;
    --icon: #8a8a8a;
  }
  * { box-sizing: border-box; margin: 0; padding: 0; }
  html, body {
    width: 1200px; height: 942px; overflow: hidden;
    background: var(--frame);
    font-family: "Rajdhani", Arial, sans-serif;
  }
  .page {
    position: absolute; left: 14px; top: 14px;
    width: 1172px; height: 914px;
    background: var(--footer-bg);
  }
  .hero {
    position: absolute; left: 0; top: 0;
    width: 1172px; height: 877px;
  }
  .hero-photo {
    position: absolute; inset: 0;
    background:
      radial-gradient(ellipse 60% 45% at 22% 78%, rgba(63,110,102,0.75), transparent 70%),
      radial-gradient(ellipse 55% 40% at 80% 80%, rgba(74,90,99,0.7), transparent 70%),
      linear-gradient(180deg, var(--night) 0%, #1b1e22 35%, var(--slate) 65%, var(--steel) 100%);
  }
  .brand {
    position: absolute; left: 22px; top: 42px;
    display: flex; align-items: center; gap: 12px;
    color: var(--logo-text);
    font-weight: 500; font-size: 20px; letter-spacing: 3px;
    text-transform: uppercase; line-height: 28px;
  }
  .brand-mark { width: 3px; height: 46px; background: var(--accent); }
  .main-nav {
    position: absolute; top: 41px; right: 16px;
    display: flex; list-style: none;
  }
  .main-nav li a {
    display: block; height: 37px; line-height: 38px;
    padding: 0 9px; margin-left: 5px;
    color: var(--nav-text); text-decoration: none;
    font-size: 14px; font-weight: 500; letter-spacing: 0.2px;
  }
  .main-nav li a.current { background: var(--accent); color: #fff; font-weight: 600; padding: 0 13px; }
  .hero-content {
    position: absolute; left: 22px; top: 330px; width: 520px;
  }
  .hero-content .kicker {
    color: var(--accent); font-size: 15px; font-weight: 600;
    letter-spacing: 3px; text-transform: uppercase; margin-bottom: 10px;
  }
  .hero-content h1 {
    color: var(--heading); font-size: 46px; font-weight: 600;
    line-height: 50px; letter-spacing: 1px; margin-bottom: 16px;
  }
  .hero-content p {
    color: var(--lead); font-size: 18px; font-weight: 500; line-height: 26px;
  }
  .site-footer {
    position: absolute; left: 0; top: 877px;
    width: 1172px; height: 37px;
    display: flex; align-items: center; justify-content: space-between;
    padding: 0 14px 0 16px;
    color: var(--footer-text); font-size: 14px; font-weight: 500;
  }
  .contact-details { display: flex; gap: 22px; }
  .social { display: flex; gap: 3px; }
  .social span {
    width: 22px; height: 22px; border-radius: 50%;
    background: var(--icon); display: block;
  }
</style>
</head>
<body>
<div class="page">
  <header class="hero">
    <div class="hero-photo" role="img" aria-label="Dimmed photograph of a high-rise under construction with tower cranes and steel scaffolding against a dark sky"></div>
    <div class="brand"><span class="brand-mark"></span>Kestrel Constructions</div>
    <ul class="main-nav">
      <li><a class="current" href="#">HOME</a></li>
      <li><a href="#">ABOUT</a></li>
      <li><a href="#">SERVICES</a></li>
      <li><a href="#">PROJECTS</a></li>
      <li><a href="#">CULTURE</a></li>
      <li><a href="#">NEWS</a></li>
      <li><a href="#">CONTACT</a></li>
    </ul>
    <section class="hero-content">
      <p class="kicker">Commercial &amp; Civil Building</p>
      <h1>Built on precision, delivered with care</h1>
      <p>From planning to handover, we manage every stage of your project with clear communication and lasting quality.</p>
    </section>
  </header>
  <footer class="site-footer">
    <p class="copyright">© 2018&nbsp; Kestrel Constructions. All Rights Reserved.</p>
    <p class="contact-details"><span>Phone 02 5550 1840</span><span>hello@kestrelconstructions.example</span></p>
    <div class="social" aria-label="Social links">
      <span></span><span></span><span></span><span></span>
    </div>
  </footer>
</div>
</body>
</html>
```